" Temos como objetivo melhor atender as demandas atuais em TI com suporte de fácil acesso e analistas especializados com certificações que o mercado atual exige. Nossa equipe se dedica à prevenção, resolução de problemas e sugestões de melhorias do ambiente para garantir que seus servidores e aplicações estejam sempre no ar e funcionando, garantindo a continuidade dos negócios, foco das nossas soluções. "

```html
<!DOCTYPE html>
<html lang="pt-BR">
<head>
<meta charset="UTF-8">
<title>Nuvara — Pasta institucional</title>
<link href="https://fonts.googleapis.com/css2?family=Montserrat:wght@500&display=swap" rel="stylesheet">
<style>
  :root{
    --backdrop:#ff6a00;
    --navy:#0e2a47;
    --paper:#ffffff;
    --accent-orange:#f47a1f;
    --accent-amber:#f6a623;
  }
  *{margin:0;padding:0;box-sizing:border-box}
  html,body{width:1200px;height:1200px;overflow:hidden}
  body{background:var(--backdrop);position:relative;font-family:"Montserrat",sans-serif}
  .folder{position:absolute;left:192px;top:197px;width:847px;height:770px}
  .folder-inside{position:absolute;left:0;top:0;width:425px;height:571px;background:var(--paper)}
  .folder-cover{position:absolute;left:425px;top:0;width:422px;height:571px;background:var(--navy);overflow:hidden}
  .cover-swoosh{position:absolute;left:0;top:0;width:422px;height:571px}
  .pocket-flap{position:absolute;left:0;top:571px;width:425px;height:199px}
  .brand{position:absolute;display:flex;align-items:center;font-weight:500;letter-spacing:.12em;line-height:1}
  .brand-dot{border-radius:50%;background:var(--accent-orange);flex:none}
  .brand--cover{left:92px;top:262px;color:var(--paper);font-size:43px;gap:16px}
  .brand--cover .brand-dot{width:40px;height:40px}
  .brand--inside{left:128px;top:466px;color:var(--navy);font-size:28px;gap:10px}
  .brand--inside .brand-dot{width:26px;height:26px}
</style>
</head>
<body>
  <div class="folder">
    <section class="folder-inside">
      <div class="brand brand--inside"><span class="brand-dot"></span><span class="brand-name">NUVARA</span></div>
    </section>
    <section class="folder-cover">
      <div class="brand brand--cover"><span class="brand-dot"></span><span class="brand-name">NUVARA</span></div>
      <svg class="cover-swoosh" viewBox="0 0 422 571" aria-hidden="true">
        <path d="M262 571 Q318 440 422 398 L422 571 Z" fill="var(--accent-orange)"/>
        <path d="M292 571 Q345 462 422 424 L422 571 Z" fill="var(--accent-amber)"/>
        <path d="M326 571 Q366 486 422 450 L422 571 Z" fill="var(--paper)"/>
      </svg>
    </section>
    <svg class="pocket-flap" viewBox="0 0 425 199" aria-hidden="true">
      <polygon points="0,0 408,0 288,199 0,199" fill="var(--navy)"/>
    </svg>
  </div>
</body>
</html>
```